Pages That Sell Services - book cover (front panel only)

I want a book cover (for print and ebook) in a distinctive, quirky style that can be repurposed for podcast artwork too. Full brief supplied.
The book is a practical, accessible handbook for anyone thinking about writing a book to build their business, with a wide range of tips and techniques to help plan, write, publishing and promote a book that’s integrated with your platform and works to build your reputation, network and credibility from day 1.
The target audience is experts in business, particularly owners of SMEs with an established online and offline platform (eg speaking, training, consulting) who want to add a book to take their business to the next level.
I want the design to be strong and distinctive, slightly quirky without being gimmicky, with the focus on typography.

Target Market(s)

Those writing a book based on their expertise to build their business

Industry/Entity Type

Publishing Company

Font styles to use
Serif
Sans Serif
Decorative

Colors

Designer to choose colors to be used in the design.

Requirements
Must have
• Commercially appealing book cover design, with application files and copyright supplied, front panel only, 5.5 x 8.5 inch format. Must work at both full size and thumbnail.
Nice to have
• A distinctive style that could be applied across other products in my portfolio.

```html
<!DOCTYPE html>
<html lang="en">
<head>
<meta charset="utf-8">
<title>Pages That Sell Services – Book Cover</title>
<link rel="stylesheet" href="https://fonts.googleapis.com/css2?family=Roboto+Condensed:wght@700&family=Montserrat:wght@600&display=swap">
<style>
  :root {
    --bg-center: #505052;
    --bg-edge: #262627;
    --title-lime: #abc33d;
    --title-teal: #0fd8a3;
    --bubble: #adc33c;
    --bubble-shade: #9db233;
    --bubble-ink: #3a4812;
    --author: #ffffff;
    --desk-top: #2e2e2f;
    --desk-warm: #3a2a20;
    --desk-bottom: #101010;
  }
  html, body {
    margin: 0;
    padding: 0;
    width: 776px;
    height: 1200px;
    overflow: hidden;
    background: var(--bg-edge);
  }
  .cover {
    position: relative;
    width: 776px;
    height: 1200px;
    background: radial-gradient(ellipse 560px 560px at 388px 560px, var(--bg-center) 0%, #3c3c3d 45%, var(--bg-edge) 100%);
    overflow: hidden;
  }
  .cover-art {
    position: absolute;
    inset: 0;
    width: 776px;
    height: 1200px;
  }
  .title-top { font-family: "Roboto Condensed", "Arial Narrow", sans-serif; font-weight: 700; fill: var(--title-lime); }
  .title-main { font-family: "Roboto Condensed", "Arial Narrow", sans-serif; font-weight: 700; fill: var(--title-teal); }
  .subtitle { font-family: "Roboto Condensed", "Arial Narrow", sans-serif; font-weight: 700; fill: var(--bubble-ink); letter-spacing: 0.5px; }
  .author { font-family: "Montserrat", Arial, sans-serif; font-weight: 600; fill: var(--author); letter-spacing: 2px; }
  .desk-scene {
    position: absolute;
    left: 0;
    top: 860px;
    width: 776px;
    height: 340px;
    background: linear-gradient(180deg, rgba(46,46,47,0) 0%, var(--desk-top) 18%, #1e1e1f 45%, var(--desk-warm) 58%, #1a1a1a 70%, var(--desk-bottom) 100%);
  }
</style>
</head>
<body>
<div class="cover">
  <div class="desk-scene" role="img" aria-label="Photograph of a closed black notebook with orange-edged pages and an orange pen resting on top, on a dark desk"></div>
  <svg class="cover-art" viewBox="0 0 776 1200" xmlns="http://www.w3.org/2000/svg">
    <text class="title-top" x="48" y="151" font-size="96" textLength="685" lengthAdjust="spacingAndGlyphs">PAGES THAT SELL</text>
    <text class="title-main" x="74" y="309" font-size="197" textLength="661" lengthAdjust="spacingAndGlyphs">SERVICES</text>

    <g class="speech-bubble">
      <polygon points="142,343 655,358 668,622 262,622 180,662 205,604 133,600" fill="var(--bubble)"/>
      <polygon points="137,512 560,622 262,622 180,662 205,604 133,600" fill="var(--bubble-shade)"/>
      <text class="subtitle" font-size="36" text-anchor="middle">
        <tspan x="398" y="428">SMART STEPS TO SHAPE</tspan>
        <tspan x="398" y="477">AND CRAFT A BOOK</tspan>
        <tspan x="398" y="526">THAT WINS YOU MORE</tspan>
        <tspan x="398" y="582">CLIENTS AND TRUST</tspan>
      </text>
    </g>

    <text class="author" x="394" y="760" font-size="76" text-anchor="middle">MEGAN HALE</text>
  </svg>
</div>
</body>
</html>
```